Business Card Design needed for logo design project

This project is linked to Dental Clinic Logo (SEE ATTACHED LOGO FOR GUIDANCE).

Our company needs a Business Card Design. Please refer to our original project in the link above.

Industry/Entity Type

Business

```html
<!DOCTYPE html>
<html lang="en">
<head>
<meta charset="utf-8">
<title>Harbourside Dental Clinic – Business Card</title>
<link rel="stylesheet" href="https://fonts.googleapis.com/css2?family=Comfortaa:wght@400;600&display=swap">
<style>
  :root {
    --backdrop: #161616;
    --green-deep: #16805f;
    --green-mid: #228a69;
    --green-light: #4f9f84;
    --mint: #5ec7a6;
    --paper: #ffffff;
    --ink: #3a3a3a;
    --pin-grey: #c9cdcb;
    --pin-shadow: rgba(0, 0, 0, 0.25);
    --label: #eef6f2;
  }
  * { margin: 0; padding: 0; box-sizing: border-box; }
  html, body {
    width: 1200px;
    height: 1134px;
    overflow: hidden;
    background: var(--backdrop);
    font-family: "Comfortaa", sans-serif;
  }
  .canvas {
    position: relative;
    width: 1200px;
    height: 1134px;
  }
  .card {
    position: absolute;
    top: 380px;
    width: 540px;
    height: 300px;
    border-radius: 2px;
    overflow: hidden;
    box-shadow: 0 14px 40px rgba(0, 0, 0, 0.55);
  }
  .card--front {
    left: 40px;
    background: radial-gradient(ellipse at 62% 18%, var(--green-light) 0%, var(--green-mid) 45%, var(--green-deep) 100%);
  }
  .card--back {
    left: 620px;
    background: var(--paper);
  }

  .wordmark {
    display: flex;
    align-items: center;
    gap: 12px;
  }
  .wordmark__dot {
    width: 22px;
    height: 22px;
    border-radius: 50%;
    background: var(--mint);
    flex: none;
  }
  .wordmark__text {
    font-weight: 600;
    line-height: 1.15;
  }
  .wordmark__name { display: block; }
  .wordmark__sub {
    display: block;
    text-transform: uppercase;
    letter-spacing: 0.42em;
  }

  .card--front .wordmark {
    position: absolute;
    left: 40px;
    top: 116px;
  }
  .card--front .wordmark__text { color: var(--paper); }
  .card--front .wordmark__name { font-size: 24px; }
  .card--front .wordmark__sub { font-size: 9px; margin-top: 4px; }
  .card--front .wordmark__dot { background: var(--paper); width: 18px; height: 18px; }

  .divider {
    position: absolute;
    left: 292px;
    top: 30px;
    width: 2px;
    height: 240px;
    background: linear-gradient(to bottom, transparent, rgba(0,0,0,0.28) 50%, transparent);
    box-shadow: 2px 0 6px rgba(0,0,0,0.18);
  }

  .contact-list {
    position: absolute;
    left: 296px;
    top: 106px;
    list-style: none;
  }
  .contact-item {
    display: flex;
    align-items: center;
    height: 30px;
    margin-bottom: 4px;
  }
  .contact-item__bar {
    width: 34px;
    height: 7px;
    background: var(--pin-grey);
    box-shadow: 0 2px 3px var(--pin-shadow);
  }
  .contact-item__icon {
    width: 20px;
    height: 20px;
    border-radius: 50%;
    background: var(--pin-grey);
    box-shadow: 0 2px 3px var(--pin-shadow);
    display: flex;
    align-items: center;
    justify-content: center;
    margin-left: -2px;
  }
  .contact-item__icon svg { width: 12px; height: 12px; }
  .contact-item__label {
    margin-left: 10px;
    font-size: 12px;
    color: var(--label);
    font-weight: 400;
  }

  .card--back .wordmark {
    position: absolute;
    left: 50%;
    top: 50%;
    transform: translate(-50%, -50%);
  }
  .card--back .wordmark__text { color: var(--ink); }
  .card--back .wordmark__name { font-size: 36px; }
  .card--back .wordmark__sub { font-size: 13px; margin-top: 6px; }
  .card--back .wordmark__dot { width: 28px; height: 28px; }

  .signature {
    position: absolute;
    left: 44px;
    top: 960px;
  }
  .signature .wordmark__text { color: #4d4d4d; }
  .signature .wordmark__name { font-size: 46px; }
  .signature .wordmark__dot { width: 34px; height: 34px; }
</style>
</head>
<body>
<main class="canvas">

  <section class="card card--front" aria-label="Card front">
    <div class="wordmark">
      <span class="wordmark__dot"></span>
      <span class="wordmark__text">
        <span class="wordmark__name">Harbourside</span>
        <span class="wordmark__sub">Dental Clinic</span>
      </span>
    </div>

    <div class="divider"></div>

    <ul class="contact-list">
      <li class="contact-item">
        <span class="contact-item__bar"></span>
        <span class="contact-item__icon">
          <svg viewBox="0 0 12 12" aria-hidden="true"><path d="M3 1.5l1.6 2.2-1 1a6 6 0 0 0 3.7 3.7l1-1 2.2 1.6-1 1.5C5.8 10.5 1.5 6.2 1.5 2.5z" fill="#1e8a68"/></svg>
        </span>
        <span class="contact-item__label">Phone Number</span>
      </li>
      <li class="contact-item">
        <span class="contact-item__bar"></span>
        <span class="contact-item__icon">
          <svg viewBox="0 0 12 12" aria-hidden="true"><rect x="1.5" y="3" width="9" height="6.5" fill="none" stroke="#1e8a68" stroke-width="1.2"/><path d="M1.8 3.3L6 6.6l4.2-3.3" fill="none" stroke="#1e8a68" stroke-width="1.2"/></svg>
        </span>
        <span class="contact-item__label">Email@</span>
      </li>
      <li class="contact-item">
        <span class="contact-item__bar"></span>
        <span class="contact-item__icon">
          <svg viewBox="0 0 12 12" aria-hidden="true"><g fill="none" stroke="#1e8a68" stroke-width="1"><circle cx="6" cy="6" r="4.5"/><ellipse cx="6" cy="6" rx="2" ry="4.5"/><path d="M1.5 6h9M2.3 3.7h7.4M2.3 8.3h7.4"/></g></svg>
        </span>
        <span class="contact-item__label">Website</span>
      </li>
    </ul>
  </section>

  <section class="card card--back" aria-label="Card back">
    <div class="wordmark">
      <span class="wordmark__dot"></span>
      <span class="wordmark__text">
        <span class="wordmark__name">Harbourside</span>
        <span class="wordmark__sub">Dental Clinic</span>
      </span>
    </div>
  </section>

  <div class="signature wordmark">
    <span class="wordmark__dot"></span>
    <span class="wordmark__text"><span class="wordmark__name">Harbourside</span></span>
  </div>

</main>
</body>
</html>
```